Harborline Hire Business Card Design

Need business cards designed for our new equipment rental. We specialize in renting to landscape / tree professionals, contractors, Do-It-Yourself'ers and Around the home or office. Looking for a eye catching card. Landscape and construction should be the theme. The logo is attached, and you can see our colors from the logo. You can use whatever color goes with it ok.

Target Market(s)

First off Landscape and Tree Professional. Then contractors, Do-It-Yourself'ers and rentals for Around the home or office.

Industry/Entity Type

Business

Contact Information for Business Card

Eye catching background that blends landscaping with construction equipment

Requirements
Must have
• Name on Card will Be: Martin Kolbeck (Manager)
• My Direct Phone Number is: 352-817-3062
• martin@harborlinehire.com
• www.harborlinehire.com
• 4712 Willow Brook Lane,
• Dade City FL 33590
Nice to have
• Would be Nice to have these bullets on the Face of the card that does not have all my information.
• Serving:
• Landscape / Tree Professionals
• Contractors
• DYI'ers or say Do-It-Yourself'ers
• Maybe have serving small and centered above these bullets, and these 3 bullets along the bottom of the card. Ideas?

```html
<!DOCTYPE html>
<html lang="en">
<head>
<meta charset="utf-8">
<title>Harborline Hire – Business Card</title>
<link rel="stylesheet" href="https://fonts.googleapis.com/css2?family=Raleway:wght@300;400;600;800&display=swap">
<style>
  :root {
    --page: #ffffff;
    --teal: #2bbdb2;
    --teal-deep: #1f978e;
    --charcoal: #26262a;
    --navy: #1d4a74;
    --ink: #111111;
    --white: #ffffff;
    --mist: #dcdcdc;
  }
  * { margin: 0; padding: 0; box-sizing: border-box; }
  html, body {
    width: 1200px;
    height: 427px;
    overflow: hidden;
    background: var(--page);
    font-family: "Raleway", Arial, sans-serif;
  }
  .sheet { position: relative; width: 1200px; height: 427px; }
  .card {
    position: absolute;
    top: 23px;
    width: 554px;
    height: 316px;
    box-shadow: 0 4px 12px rgba(0, 0, 0, 0.45);
    overflow: hidden;
  }
  .card svg { display: block; width: 100%; height: 100%; }
  .card--front { left: 23px; }
  .card--back { left: 619px; }
  .side-label {
    position: absolute;
    top: 368px;
    width: 554px;
    text-align: center;
    font-size: 42px;
    font-weight: 400;
    letter-spacing: 2px;
    color: var(--ink);
  }
  .side-label--front { left: 23px; }
  .side-label--back { left: 619px; }
  .brand-name { font-family: "Raleway", Arial, sans-serif; font-weight: 800; }
  .card-text { font-family: "Raleway", Arial, sans-serif; }
</style>
</head>
<body>
<div class="sheet">

  <!-- Front side -->
  <div class="card card--front">
    <svg viewBox="0 0 526 300" xmlns="http://www.w3.org/2000/svg">
      <defs>
        <linearGradient id="front-photo-tone" x1="0" y1="0" x2="1" y2="1">
          <stop offset="0" stop-color="#f1f1f1"/>
          <stop offset="0.5" stop-color="#d4d4d4"/>
          <stop offset="1" stop-color="#bdbdbd"/>
        </linearGradient>
      </defs>
      <rect class="front-photo" width="526" height="300" fill="url(#front-photo-tone)"
            role="img" aria-label="Faded grey photo of backhoes and excavators on a construction site"/>
      <polygon class="light-beam" points="0,48 526,96 526,150 0,78" fill="#ffffff" opacity="0.35"/>
      <polygon class="light-beam" points="120,150 526,110 526,200 260,230" fill="#ffffff" opacity="0.25"/>

      <path class="base-band" d="M0,262 C150,248 330,236 526,258 L526,300 L0,300 Z" fill="var(--charcoal)"/>
      <path class="swoosh swoosh--back" d="M0,238 C50,228 100,232 150,250 C100,244 50,246 0,258 Z" fill="var(--teal-deep)"/>
      <path class="swoosh swoosh--front" d="M112,250 C250,226 410,226 526,234 L526,252 C410,246 260,252 116,274 Z" fill="var(--teal)"/>

      <text class="brand-name" x="263" y="142" text-anchor="middle" font-size="32" fill="var(--navy)">HARBORLINE HIRE</text>

      <g class="serving-list">
        <text class="card-text" x="263" y="192" text-anchor="middle" font-size="7" font-weight="600" letter-spacing="2" fill="var(--charcoal)">SERVING</text>
        <text class="card-text" x="263" y="207" text-anchor="middle" font-size="8.5" font-weight="600" fill="var(--charcoal)">Landscape / Tree Professionals  •  Contractors  •  Do-It-Yourself'ers</text>
      </g>

      <text class="card-text" x="263" y="292" text-anchor="middle" font-size="11" font-weight="600" fill="var(--white)">www.harborlinehire.com</text>
    </svg>
  </div>
  <div class="side-label side-label--front">FRONT</div>

  <!-- Back side -->
  <div class="card card--back">
    <svg viewBox="0 0 526 300" xmlns="http://www.w3.org/2000/svg">
      <defs>
        <linearGradient id="mower-photo-tone" x1="0" y1="0" x2="1" y2="1">
          <stop offset="0" stop-color="#404244"/>
          <stop offset="1" stop-color="#28292b"/>
        </linearGradient>
        <linearGradient id="house-photo-tone" x1="0" y1="0" x2="1" y2="1">
          <stop offset="0" stop-color="#2e3a34"/>
          <stop offset="0.55" stop-color="#4a4a33"/>
          <stop offset="1" stop-color="#2b3626"/>
        </linearGradient>
      </defs>
      <rect class="mower-photo" width="330" height="300" fill="url(#mower-photo-tone)"
            role="img" aria-label="Darkened photo of ride-on lawn mowers on a lawn"/>
      <rect class="house-photo" x="318" width="208" height="300" fill="url(#house-photo-tone)"
            role="img" aria-label="Photo of a lit house and landscaped garden at dusk"/>

      <polygon class="light-beam" points="526,0 526,30 120,180 100,150" fill="#ffffff" opacity="0.18"/>
      <polygon class="light-beam" points="526,20 526,60 170,240 150,205" fill="#ffffff" opacity="0.14"/>

      <path class="divider-curve" d="M318,0 L338,0 C352,70 340,190 322,300 L310,300 C324,190 330,80 318,0 Z" fill="var(--teal)"/>
      <path class="divider-fold" d="M325,70 C338,110 334,160 318,200 C324,160 326,115 320,80 Z" fill="var(--teal-deep)"/>

      <text class="brand-name" x="150" y="140" text-anchor="middle" font-size="22" fill="var(--teal)">MARTIN <tspan font-weight="400">KOLBECK</tspan></text>
      <text class="card-text" x="150" y="162" text-anchor="middle" font-size="12" font-weight="400" fill="var(--white)">MANAGER</text>

      <!-- contact rows -->
      <g class="contact-icon icon-mail" fill="var(--teal)">
        <rect x="38" y="238" width="10" height="7"/>
        <path d="M38,238 L43,242 L48,238" stroke="#2a2b2d" stroke-width="1" fill="none"/>
      </g>
      <text class="card-text" x="57" y="244.5" font-size="7.5" fill="var(--white)">martin@harborlinehire.com</text>

      <path class="contact-icon icon-phone" d="M178,237 l3,0 l1,3 l-2,1 a7,7 0 0 0 4,4 l1,-2 l3,1 l0,3 a9,9 0 0 1 -10,-10 Z" fill="var(--teal)"/>
      <text class="card-text" x="196" y="244.5" font-size="7.5" fill="var(--white)">352-817-3062</text>

      <path class="contact-icon icon-pin" d="M43,261 a4.5,4.5 0 0 1 4.5,4.5 c0,3.5 -4.5,8 -4.5,8 c0,0 -4.5,-4.5 -4.5,-8 a4.5,4.5 0 0 1 4.5,-4.5 Z M43,264 a1.6,1.6 0 1 0 0.01,0 Z" fill="var(--teal)" fill-rule="evenodd"/>
      <text class="card-text" x="57" y="268.5" font-size="7.5" fill="var(--white)">4712 Willow Brook Lane,</text>
      <text class="card-text" x="57" y="278.5" font-size="7.5" fill="var(--white)">Dade City FL 33590</text>

      <g class="contact-icon icon-globe" fill="none" stroke="var(--teal)" stroke-width="1">
        <circle cx="183" cy="266" r="5"/>
        <ellipse cx="183" cy="266" rx="2.2" ry="5"/>
        <line x1="178" y1="266" x2="188" y2="266"/>
      </g>
      <text class="card-text" x="196" y="268.5" font-size="7.5" fill="var(--white)">www.harborlinehire.com</text>

      <text class="brand-name" x="475" y="287" text-anchor="middle" font-size="10" fill="var(--mist)">HARBORLINE HIRE</text>
    </svg>
  </div>
  <div class="side-label side-label--back">BACK</div>

</div>
</body>
</html>
```